I would like to purchase a customized version of a design you have previously submitted - https://www.artvaultly.com/design/58314720
hi
would like the design about the some. just with our  details and logo
office number 01563829140
Mobil number 07812645037
web sparlowcleaning.ltd
email sparlowcleaning@mailtrove.co.uk
on the back we would like to put a price list

```html
<!DOCTYPE html>
<html lang="en">
<head>
<meta charset="utf-8">
<title>Sparlow Cleaning &amp; Maintenance – Flyer Front and Price List</title>
<link href="https://fonts.googleapis.com/css2?family=Poppins:wght@400;500;600;700&display=swap" rel="stylesheet">
<style>
:root{
  --navy:#2b2c8c;
  --royal:#2f5fc8;
  --blue:#3f86cf;
  --blue-deep:#2f6fbd;
  --magenta:#e2399b;
  --ink:#2a2a3a;
  --page-bg:#eef0f3;
  --white:#ffffff;
}
*{margin:0;padding:0;box-sizing:border-box}
html,body{width:845px;height:1200px;overflow:hidden;background:var(--page-bg)}
body{font-family:"Poppins",sans-serif;color:var(--ink);position:relative}

.sheet{position:absolute;left:198px;width:449px;height:580px;overflow:hidden;background:#fff;box-shadow:0 2px 8px rgba(0,0,0,.15)}
.sheet-front{top:10px}
.sheet-back{top:610px}
.page{position:absolute;left:0;top:0;width:648px;height:838px;transform:scale(.6925);transform-origin:0 0;overflow:hidden;background:#fff}
.page > svg{position:absolute;left:0;top:0}
.abs{position:absolute}

/* ---------- front ---------- */
.brand{left:395px;top:34px;width:230px;text-align:center;color:var(--royal);font-weight:700}
.brand-name{font-size:44px;line-height:1;letter-spacing:1px}
.brand-sub{font-size:12.5px;margin-top:4px;white-space:nowrap}

.headline{left:302px;top:343px;color:var(--royal);font-weight:700;font-size:31px;line-height:1.05;white-space:nowrap}
.headline .dark{color:var(--navy)}
.subhead{left:302px;top:430px;font-size:18.5px;line-height:1.15;color:#333;white-space:nowrap}
.subhead b{font-weight:600}

.pill{left:0;background:#fff;border-radius:0 16px 16px 0;height:30px;width:163px;font-weight:700;font-size:19px;padding-left:36px;line-height:32px;color:var(--navy)}
.pill .accent{color:var(--magenta)}
.about-pill{top:438px}
.service-pill{top:577px}
.about-text{left:36px;top:480px;width:218px;color:#fff;font-size:9.6px;line-height:1.27}
.service-list{left:36px;top:616px;list-style:none;color:#fff;font-weight:500;font-size:12.5px}
.service-list li{height:21px;display:flex;align-items:center;gap:8px}
.service-list li::before{content:"";width:7px;height:7px;border:1.3px solid #fff;border-radius:50%}

.benefits-bar{left:280px;top:488px;width:228px;height:33px;background:var(--magenta);border-radius:0 16px 16px 0;color:#fff;font-weight:600;font-size:20px;line-height:35px;padding-left:22px}
.benefits-intro{left:302px;top:530px;width:300px;font-size:9.8px;line-height:1.27;color:#333}
.benefit-list{left:302px;top:600px;list-style:none;font-size:11px;color:#333}
.benefit-list li{height:21px;display:flex;align-items:center;gap:10px}
.benefit-list li::before{content:"";width:6px;height:6px;border-radius:50%;background:var(--blue)}

.cta{left:237px;top:723px;width:176px;height:30px;background:#fff;border:1.2px solid var(--royal);color:var(--magenta);font-weight:500;font-size:13px;text-align:center;line-height:28px}
.cta b{font-weight:700}

.foot-book{color:#fff;font-size:9.5px;font-weight:500}
.foot-phone{color:#fff;font-weight:600;display:flex;align-items:center;gap:6px;letter-spacing:.4px;white-space:nowrap}
.foot-office{font-size:10.5px}
.foot-office .num{font-weight:500;display:flex;align-items:center;gap:6px;white-space:nowrap}
.foot-links{font-size:10px;line-height:1.7}
.foot-links div{display:flex;align-items:center;gap:8px;white-space:nowrap}
.foot-links b{font-weight:600}

.front .foot-book{left:36px;top:770px}
.front .foot-phone{left:34px;top:781px;font-size:24px}
.front .foot-office{left:280px;top:777px;color:#fff}
.front .foot-office .num{font-size:15px}
.front .foot-links{left:435px;top:780px;color:#fff}

/* ---------- back ---------- */
.tag{display:inline-block;background:var(--magenta);color:#fff;font-weight:600;font-size:12.5px;line-height:20px;padding:0 7px;letter-spacing:.3px}
.col{position:absolute;width:275px}
.col-left{left:35px}
.col-right{left:340px}
.col-top{top:36px}
.col-band{top:330px}
.divider{position:absolute;left:322px;border-left:1.5px dotted var(--blue)}

.item{display:flex;justify-content:space-between;align-items:flex-start;height:89px;padding-top:6px}
.col-top .item + .item{border-top:1.3px dotted var(--navy)}
.col-top .tag + .item{height:83px;padding-top:0}
.col-band .item{height:88px;padding-top:0}
.item-title{font-size:14px;color:var(--navy);white-space:nowrap;line-height:1.3}
.item-title b{font-weight:700}
.bullets{list-style:none;font-size:9.5px;margin-top:3px}
.bullets li{height:15.5px;display:flex;align-items:center;gap:7px;white-space:nowrap;color:#333}
.bullets li::before{content:"";width:5px;height:5px;border-radius:50%;background:var(--blue)}
.bullets em{font-style:normal;font-weight:600;color:var(--royal)}

.col-band .item-title{color:#fff}
.col-band .bullets li{color:#fff}
.col-band .bullets li::before{background:none;border:1px solid #fff;width:6px;height:6px}
.col-band .bullets em{color:#fff}

.price{width:67px;height:62px;border-radius:4px;overflow:hidden;flex:none;display:flex;flex-direction:column;text-align:center}
.price .amt{flex:1;background:var(--blue);color:#fff;font-weight:600;font-size:27px;line-height:44px}
.price .amt sup{font-size:13px;vertical-align:top;line-height:28px;margin-right:1px}
.price .per{background:var(--navy);color:#fff;font-size:9.5px;font-weight:500;line-height:17px}
.price.alt .amt{background:#fff;color:var(--royal)}
.price.alt .per{background:var(--magenta)}
.price.wide{width:78px}

.other-tag{left:215px;top:499px}
.other{position:absolute;left:35px;top:520px;width:578px}
.other-row{display:flex;align-items:center;height:72px}
.other-row + .other-row{border-top:1.3px dotted var(--navy)}
.other-title{width:305px;font-weight:700;font-size:13.5px;color:var(--navy);white-space:nowrap}
.other-row .bullets{width:195px;margin:0}

.back .foot-book{left:35px;top:777px}
.back .foot-phone{left:33px;top:790px;font-size:26px}
.back .foot-office{left:445px;top:757px;color:#333}
.back .foot-office .num{font-size:16px}
.back .foot-links{left:445px;top:794px;color:#333;font-size:9.5px;line-height:1.6}
.back .foot-links b{color:var(--royal)}
</style>
</head>
<body>

<!-- front side -->
<div class="sheet sheet-front">
<div class="page front">
  <svg width="648" height="838" viewBox="0 0 648 838" xmlns="http://www.w3.org/2000/svg">
    <defs>
      <linearGradient id="windowPhoto" x1="0" y1="0" x2="1" y2="1">
        <stop offset="0" stop-color="#dfe6e8"/><stop offset=".5" stop-color="#b9c7c6"/><stop offset="1" stop-color="#8ea487"/>
      </linearGradient>
      <linearGradient id="workerPhoto" x1="0" y1="0" x2="1" y2="1">
        <stop offset="0" stop-color="#d3dbde"/><stop offset=".6" stop-color="#a9bfc9"/><stop offset="1" stop-color="#5e7fa0"/>
      </linearGradient>
      <linearGradient id="column" x1="0" y1="0" x2="0" y2="1">
        <stop offset="0" stop-color="#4b93d9"/><stop offset="1" stop-color="#3373c2"/>
      </linearGradient>
      <linearGradient id="greyPanel" x1="0" y1="0" x2="1" y2="0">
        <stop offset="0" stop-color="#f4f4f6"/><stop offset="1" stop-color="#e4e4e8"/>
      </linearGradient>
    </defs>
    <rect x="0" y="0" width="648" height="340" fill="url(#windowPhoto)" role="img" aria-label="Photo of a water-fed pole cleaning a large window"/>
    <path d="M230 0 C320 90 440 150 648 170 L648 0 Z" fill="#fff"/>
    <path d="M185 0 L230 0 C320 90 440 150 648 170 L648 192 C440 176 300 110 185 0 Z" fill="var(--navy)"/>
    <path d="M255 322 C380 286 520 276 648 284 L648 760 L255 760 Z" fill="var(--blue-deep)"/>
    <rect x="0" y="300" width="282" height="460" fill="url(#column)"/>
    <path d="M290 338 C400 308 540 300 648 306 L648 750 L222 750 C256 620 276 480 290 338 Z" fill="#fff"/>
    <path d="M262 592 L648 592 L648 750 L222 750 C236 700 250 645 262 592 Z" fill="url(#greyPanel)"/>
    <path d="M0 205 L190 205 C235 205 265 260 262 310 C258 370 225 410 180 415 L0 415 Z" fill="url(#workerPhoto)" stroke="#fff" stroke-width="5" role="img" aria-label="Photo of a cleaner in yellow gloves wiping a window"/>
    <rect x="0" y="750" width="648" height="88" fill="var(--navy)"/>
  </svg>

  <div class="abs brand">
    <div class="brand-name">SPARLOW</div>
    <div class="brand-sub">CLEANING &amp; MAINTENANCE LTD</div>
  </div>

  <h1 class="abs headline">Reliable Window<br><span class="dark">cleaning services</span></h1>
  <p class="abs subhead">For Residential &amp; Commercial<br>customers in &amp; <b>around Essex</b></p>

  <div class="abs pill about-pill"><span class="accent">About</span> Us</div>
  <p class="abs about-text">Sparlow Cleaning Ltd have been cleaning windows for commercial and residential properties throughout Hutton, Shenfield &amp; the surrounding areas since 1999. We cover most towns in Essex including Brentwood, Chelmsford, Romford, Loughton and Billericay.</p>

  <div class="abs pill service-pill"><span class="accent">Our</span> Service</div>
  <ul class="abs service-list">
    <li>Window Cleaning</li>
    <li>Conservatory Cleaning</li>
    <li>Pressure washing</li>
    <li>Gutter cleaning</li>
    <li>Soffits &amp; Fascia cleaning</li>
  </ul>

  <div class="abs benefits-bar">Our Benifits</div>
  <p class="abs benefits-intro">Pure Water Fed Pole Systems are the future for the window cleaning industry, as they comply with Health and Safety Laws.They also offer lots of other benefits for our customers including:</p>
  <ul class="abs benefit-list">
    <li>Reduces disturbance to building occupants</li>
    <li>Cleaning up to 50 feet from the safety of the ground</li>
    <li>Frames cleaned as standard</li>
    <li>Cleaning of windows that ladders could not reach</li>
    <li>Reduces the cost of window cleaning.</li>
  </ul>

  <div class="abs cta">CONTACT US <b>TODAY!</b></div>

  <div class="abs foot-book">Ready to book Window Cleaning</div>
  <div class="abs foot-phone">
    <svg width="20" height="20" viewBox="0 0 24 24" aria-hidden="true"><path d="M6.6 10.8a15 15 0 0 0 6.6 6.6l2.2-2.2a1 1 0 0 1 1-.25 11.4 11.4 0 0 0 3.6.57 1 1 0 0 1 1 1V20a1 1 0 0 1-1 1A17 17 0 0 1 3 4a1 1 0 0 1 1-1h3.5a1 1 0 0 1 1 1c0 1.25.2 2.45.57 3.57a1 1 0 0 1-.25 1z" fill="var(--magenta)"/></svg>
    <span>07812 645037</span>
  </div>
  <div class="abs foot-office">Office Number
    <div class="num"><svg width="11" height="13" viewBox="0 0 14 16" aria-hidden="true"><rect width="14" height="16" rx="2" fill="var(--magenta)"/><rect x="3" y="3" width="8" height="4" fill="#fff"/><rect x="3" y="9" width="3" height="3" fill="#fff"/><rect x="8" y="9" width="3" height="3" fill="#fff"/></svg><span>01563829140</span></div>
  </div>
  <div class="abs foot-links">
    <div><svg width="12" height="9" viewBox="0 0 15 11" aria-hidden="true"><rect width="15" height="11" rx="1.5" fill="var(--magenta)"/><path d="M1 1.5 7.5 6.5 14 1.5" stroke="#fff" stroke-width="1.3" fill="none"/></svg><span>sparlowcleaning@mailtrove.co.uk</span></div>
    <div><svg width="11" height="11" viewBox="0 0 14 14" aria-hidden="true"><circle cx="7" cy="7" r="6.3" fill="none" stroke="var(--magenta)" stroke-width="1.4"/><ellipse cx="7" cy="7" rx="2.6" ry="6.3" fill="none" stroke="var(--magenta)" stroke-width="1.2"/><path d="M.8 7h12.4" stroke="var(--magenta)" stroke-width="1.2"/></svg><span>www.<b>sparlowcleaning</b>.ltd</span></div>
  </div>
</div>
</div>

<!-- back side: price list -->
<div class="sheet sheet-back">
<div class="page back">
  <svg width="648" height="838" viewBox="0 0 648 838" xmlns="http://www.w3.org/2000/svg">
    <rect x="0" y="320" width="648" height="190" fill="var(--blue)"/>
    <path d="M0 760 C170 746 300 770 420 838 L0 838 Z" fill="var(--navy)"/>
    <path d="M180 749 C300 748 385 790 452 838 L422 838 C330 778 250 756 180 749 Z" fill="var(--magenta)"/>
  </svg>

  <div class="divider" style="top:36px;height:272px"></div>
  <div class="divider" style="top:330px;height:170px;border-color:#fff"></div>

  <div class="col col-left col-top">
    <span class="tag">EVERY 4 WEEK</span>
    <div class="item">
      <div><div class="item-title"><b>Semi Detached</b> (3/4 Bed)</div>
        <ul class="bullets"><li>Conservatory roofs from <em>£60.00</em></li><li>Drives from <em>£120.00</em></li><li>Gutters from <em>£60.00</em></li></ul></div>
      <div class="price"><div class="amt"><sup>£</sup>14</div><div class="per">PER VISIT</div></div>
    </div>
    <div class="item">
      <div><div class="item-title"><b>Detached</b> (3/4 Bed)</div>
        <ul class="bullets"><li>Conservatory roofs from <em>£60.00</em></li><li>Drives from <em>£120.00</em></li><li>Gutters from <em>£60.00</em></li></ul></div>
      <div class="price"><div class="amt"><sup>£</sup>16</div><div class="per">PER VISIT</div></div>
    </div>
    <div class="item">
      <div><div class="item-title"><b>Detached</b> (5 Bed)</div>
        <ul class="bullets"><li>Conservatory roofs from <em>£60.00</em></li><li>Drives from <em>£120.00</em></li><li>Gutters from <em>£60.00</em></li></ul></div>
      <div class="price"><div class="amt"><sup>£</sup>23</div><div class="per">PER VISIT</div></div>
    </div>
  </div>

  <div class="col col-right col-top">
    <span class="tag">EVERY 8 WEEK</span>
    <div class="item">
      <div><div class="item-title"><b>Semi Detached</b> (3/4 Bed)</div>
        <ul class="bullets"><li>Conservatory roofs from <em>£60.00</em></li><li>Drives from <em>£120.00</em></li><li>Gutters from <em>£60.00</em></li></ul></div>
      <div class="price"><div class="amt"><sup>£</sup>20</div><div class="per">PER VISIT</div></div>
    </div>
    <div class="item">
      <div><div class="item-title"><b>Detached</b> (3/4 Bed)</div>
        <ul class="bullets"><li>Conservatory roofs from <em>£60.00</em></li><li>Drives from <em>£120.00</em></li><li>Gutters from <em>£60.00</em></li></ul></div>
      <div class="price"><div class="amt"><sup>£</sup>24</div><div class="per">PER VISIT</div></div>
    </div>
    <div class="item">
      <div><div class="item-title"><b>Detached</b> (5 Bed)</div>
        <ul class="bullets"><li>Conservatory roofs from <em>£60.00</em></li><li>Drives from <em>£120.00</em></li><li>Gutters from <em>£60.00</em></li></ul></div>
      <div class="price"><div class="amt"><sup>£</sup>30</div><div class="per">PER VISIT</div></div>
    </div>
  </div>

  <div class="col col-left col-band">
    <div class="item">
      <div><div class="item-title"><b>Terrace</b> (front only)</div>
        <ul class="bullets"><li>Conservatory roofs from <em>£60.00</em></li><li>Drives from <em>£120.00</em></li><li>Gutters from <em>£60.00</em></li></ul></div>
      <div class="price alt"><div class="amt"><sup>£</sup>10</div><div class="per">PER VISIT</div></div>
    </div>
    <div class="item">
      <div><div class="item-title"><b>Terrace</b> (front &amp; back)</div>
        <ul class="bullets"><li>Conservatory roofs from <em>£60.00</em></li><li>Drives from <em>£120.00</em></li><li>Gutters from <em>£60.00</em></li></ul></div>
      <div class="price alt"><div class="amt"><sup>£</sup>14</div><div class="per">PER VISIT</div></div>
    </div>
  </div>

  <div class="col col-right col-band">
    <div class="item">
      <div><div class="item-title"><b>Terrace</b> (front only)</div>
        <ul class="bullets"><li>Conservatory roofs from <em>£60.00</em></li><li>Drives from <em>£120.00</em></li><li>Gutters from <em>£60.00</em></li></ul></div>
      <div class="price alt"><div class="amt"><sup>£</sup>15</div><div class="per">PER VISIT</div></div>
    </div>
    <div class="item">
      <div><div class="item-title"><b>Terrace</b> (front &amp; back)</div>
        <ul class="bullets"><li>Conservatory roofs from <em>£60.00</em></li><li>Drives from <em>£120.00</em></li><li>Gutters from <em>£60.00</em></li></ul></div>
      <div class="price alt"><div class="amt"><sup>£</sup>20</div><div class="per">PER VISIT</div></div>
    </div>
  </div>

  <span class="abs tag other-tag">OTHER CLEANING SERVICES</span>

  <div class="other">
    <div class="other-row">
      <div class="other-title">Conservatory Roof Cleaning from</div>
      <ul class="bullets"><li>Drives from <em>£120.00</em></li><li>Gutters from <em>£60.00</em></li></ul>
      <div class="price wide"><div class="amt"><sup>£</sup>120</div><div class="per">PER VISIT</div></div>
    </div>
    <div class="other-row">
      <div class="other-title">Driveways &amp; Patio Cleaning from</div>
      <ul class="bullets"><li>Conservatory roofs from <em>£60.00</em></li><li>Gutters from <em>£60.00</em></li></ul>
      <div class="price wide"><div class="amt"><sup>£</sup>120</div><div class="per">PER VISIT</div></div>
    </div>
    <div class="other-row">
      <div class="other-title">Gutter Cleaning from</div>
      <ul class="bullets"><li>Gutter Cleaning from <em>£60.00</em></li><li>Drives from <em>£120.00</em></li></ul>
      <div class="price wide"><div class="amt"><sup>£</sup>60</div><div class="per">PER VISIT</div></div>
    </div>
  </div>

  <div class="abs foot-book">Ready to book Window Cleaning</div>
  <div class="abs foot-phone">
    <svg width="21" height="21" viewBox="0 0 24 24" aria-hidden="true"><path d="M6.6 10.8a15 15 0 0 0 6.6 6.6l2.2-2.2a1 1 0 0 1 1-.25 11.4 11.4 0 0 0 3.6.57 1 1 0 0 1 1 1V20a1 1 0 0 1-1 1A17 17 0 0 1 3 4a1 1 0 0 1 1-1h3.5a1 1 0 0 1 1 1c0 1.25.2 2.45.57 3.57a1 1 0 0 1-.25 1z" fill="var(--magenta)"/></svg>
    <span>07812 645037</span>
  </div>
  <div class="abs foot-office">Office Number
    <div class="num"><svg width="11" height="13" viewBox="0 0 14 16" aria-hidden="true"><rect width="14" height="16" rx="2" fill="var(--magenta)"/><rect x="3" y="3" width="8" height="4" fill="#fff"/><rect x="3" y="9" width="3" height="3" fill="#fff"/><rect x="8" y="9" width="3" height="3" fill="#fff"/></svg><span>01563829140</span></div>
  </div>
  <div class="abs foot-links">
    <div><svg width="11" height="8" viewBox="0 0 15 11" aria-hidden="true"><rect width="15" height="11" rx="1.5" fill="var(--magenta)"/><path d="M1 1.5 7.5 6.5 14 1.5" stroke="#fff" stroke-width="1.3" fill="none"/></svg><span>sparlowcleaning@mailtrove.co.uk</span></div>
    <div><svg width="10" height="10" viewBox="0 0 14 14" aria-hidden="true"><circle cx="7" cy="7" r="6.3" fill="none" stroke="var(--magenta)" stroke-width="1.4"/><ellipse cx="7" cy="7" rx="2.6" ry="6.3" fill="none" stroke="var(--magenta)" stroke-width="1.2"/><path d="M.8 7h12.4" stroke="var(--magenta)" stroke-width="1.2"/></svg><span>www.<b>sparlowcleaning</b>.ltd</span></div>
  </div>
</div>
</div>

</body>
</html>
```